Lumora Wellness - Professional Sales Presentation

Lumora Wellness needs to take it's professional sales presentation to the next level. The finished product must be engaging, elegant and trustworthy. In 20 slides or less, our value proposition needs to be crisply communicated. We will be using this presentation for Webinars and in print form, so this project requires a designer with deep powerpoint presentation experience. Both are very important ... 1) How the presentation is revealed live, and 2) How it appears in print form.

I've attached a draft presentation along with AI and JPG versions of our logo. Please visit LumoraWellness.example for insight on our services. Be certain to watch the video on our home page to learn what we do ... you'll be inspired! The winning presentation will be presented in boardrooms at Meridian 700 companies across America.

I'll interact frequently with those who take this project seriously and bring their very best work to the table ... you'll be working directly with Lumora's CEO.

You're invited to knock my socks off :)

Gregor

Target Market(s)

Meridian 700 Executives - the head of Benefits or Human Resources

Industry/Entity Type

Health Care

Font styles to use
Sans Serif
Script

Colors
ec1f27

Requirements
Must have
• Must be very professional, but creatively engaging, no more than 20 slides. Board rooms are inundated with BORING presentations ... that can't be this one. It needs to stand out, without going over the top.
Nice to have
• I need to be able to edit the text you'll find in my DRAFT presentation so please don't just create and use graphic files. Feel free to create cool graphic elements that are revealed at various points, but the next needs to be editable throughout.
Should not have
• Can't be cheesy, cheap or gimmicky. Must be completely credible.

```html
<!DOCTYPE html>
<html lang="en">
<head>
<meta charset="utf-8">
<title>How's the Current Paradigm Working for You? — Lumora Wellness</title>
<link rel="stylesheet" href="https://fonts.googleapis.com/css2?family=Roboto:wght@400;700&family=Roboto+Condensed:wght@700&display=swap">
<style>
  :root {
    --brand-red: #ec1f27;
    --ink: #2b2b2b;
    --paper: #ffffff;
    --footer-ink: #ffffff;
  }
  * { margin: 0; padding: 0; box-sizing: border-box; }
  html, body { width: 1200px; height: 900px; overflow: hidden; background: var(--paper); }
  .slide {
    position: relative;
    width: 1200px;
    height: 900px;
    background: var(--paper);
    font-family: "Roboto", Arial, sans-serif;
    color: var(--ink);
    overflow: hidden;
  }
  .slide-title {
    position: absolute;
    left: 26px;
    top: 22px;
    font-family: "Roboto Condensed", "Arial Narrow", sans-serif;
    font-weight: 700;
    font-size: 36px;
    color: var(--brand-red);
    letter-spacing: -0.2px;
  }
  .title-rule {
    position: absolute;
    left: 0;
    top: 70px;
    width: 720px;
    height: 3px;
    background: var(--brand-red);
  }
  .brand-name {
    position: absolute;
    right: 36px;
    top: 20px;
    font-family: "Roboto Condensed", "Arial Narrow", sans-serif;
    font-weight: 700;
    font-size: 36px;
    color: var(--brand-red);
  }
  .question-list { list-style: none; }
  .question {
    position: absolute;
    left: 78px;
    font-size: 21.5px;
    line-height: 36px;
    white-space: nowrap;
  }
  .question-marker {
    position: absolute;
    left: -54px;
    top: 4px;
    width: 28px;
    height: 28px;
  }
  .closing-question {
    position: absolute;
    left: 78px;
    top: 740px;
    font-weight: 700;
    font-size: 25px;
    color: var(--brand-red);
    white-space: nowrap;
  }
  .closing-hint {
    position: absolute;
    left: 78px;
    top: 776px;
    font-weight: 700;
    font-size: 15px;
    color: var(--ink);
  }
  .footer-band {
    position: absolute;
    left: 0;
    bottom: 0;
    width: 1200px;
    height: 90px;
  }
  .footer-credit {
    position: absolute;
    left: 12px;
    bottom: 12px;
    font-size: 18px;
    color: var(--footer-ink);
  }
  .footer-credit .site { font-weight: 700; }
  .page-number {
    position: absolute;
    right: 60px;
    bottom: 12px;
    font-weight: 700;
    font-size: 20px;
    color: var(--ink);
  }
</style>
</head>
<body>
<svg width="0" height="0" style="position:absolute" aria-hidden="true">
  <defs>
    <symbol id="plus-marker" viewBox="0 0 28 28">
      <path d="M10 2.5 H18 V10 H25.5 V18 H18 V25.5 H10 V18 H2.5 V10 H10 Z" fill="none" stroke="#ec1f27" stroke-width="3" stroke-linejoin="round"/>
    </symbol>
  </defs>
</svg>

<main class="slide">
  <h1 class="slide-title">How’s the Current Paradigm Working for You?</h1>
  <div class="title-rule"></div>
  <div class="brand-name">Lumora Wellness</div>

  <ul class="question-list">
    <li class="question" style="top:129px">
      <svg class="question-marker"><use href="#plus-marker"/></svg>
      What percentage of your employees are getting their periodic preventive visits with a PCP?
    </li>
    <li class="question" style="top:206px">
      <svg class="question-marker"><use href="#plus-marker"/></svg>
      When you conduct biometric screenings, what, beyond participation, is defined as success?
    </li>
    <li class="question" style="top:284px">
      <svg class="question-marker"><use href="#plus-marker"/></svg>
      Why do companies do biometric screenings in the first place? (Hint: Because people don’t get their<br>periodic preventive visits)
    </li>
    <li class="question" style="top:401px">
      <svg class="question-marker"><use href="#plus-marker"/></svg>
      What percentage of those identified as needing to see a PCP for “out of range” biometrics<br>actually see one in a timely way?
    </li>
    <li class="question" style="top:518px">
      <svg class="question-marker"><use href="#plus-marker"/></svg>
      What percentage of high risk employees are engaging with your disease and health/wellness<br>programs?
    </li>
    <li class="question" style="top:636px">
      <svg class="question-marker"><use href="#plus-marker"/></svg>
      What percentage of the “screening” results are re-run by a PCP, either because they don’t receive them<br>or they doubt their accuracy?
    </li>
  </ul>

  <p class="closing-question">What are the true costs of your current “screen – refer – PCP visit – retest” paradigm?</p>
  <p class="closing-hint">(Hint: About $300, all in)</p>

  <svg class="footer-band" viewBox="0 0 1200 90" preserveAspectRatio="none" aria-hidden="true">
    <path d="M0 22 H740 C860 18 960 50 1050 90 H0 Z" fill="#ec1f27"/>
  </svg>
  <p class="footer-credit">©2015 Lumora Wellness &nbsp;• All Rights Reserved. &nbsp;| &nbsp;<span class="site">www.LumoraWellness.example</span></p>
  <p class="page-number">PAGE : 01</p>
</main>
</body>
</html>
```